比較的、ご年配の方も多いのですが、自由診療をメインに行っておりますので、高級感があるように作成をしていただけたらと思います。データはai形式で頂ける方でお願い致します。
表面:医院名・役職・電話番号・FAX・mail・住所・HPのURL 裏面::ロゴのみ(添付したロゴデザインの左)
緑系
• イラストレーター形式 (.ai)
ロゴデータが添付されておりませんでしたので、添付します。

医院のスタッフと多数決にて決定させていただきました。
シンプルながら、非常に落ち着いたデザインであることが当選の理由です。

多くの方々に提案して頂き、心よりお礼を申し上げます。素晴らしいデザインが多く非常に悩みました。
今後とも、引き続きどうぞ宜しくお願い申し上げます。

```html
<!DOCTYPE html>
<html lang="ja">
<head>
<meta charset="utf-8">
<title>桜川歯科医院 名刺</title>
<link href="https://fonts.googleapis.com/css2?family=Noto+Sans+JP:wght@400;500&family=Noto+Serif+JP:wght@400;500&display=swap" rel="stylesheet">
<style>
  :root {
    --clinic-green: #43b48a;
    --ink: #333333;
    --ink-soft: #666666;
    --paper: #ffffff;
    --backdrop: #eeeeee;
    --label: #999999;
  }
  * { margin: 0; padding: 0; box-sizing: border-box; }
  html, body { width: 900px; height: 1200px; overflow: hidden; }
  body {
    background: var(--backdrop);
    font-family: "Noto Sans JP", sans-serif;
    color: var(--ink);
    position: relative;
  }
  .side-label {
    position: absolute;
    left: 0; width: 900px;
    text-align: center;
    font-size: 15px;
    color: var(--label);
  }
  .card {
    position: absolute;
    left: 150px;
    width: 600px;
    height: 364px;
    box-shadow: 0 2px 8px rgba(0,0,0,0.12);
  }
  .card-front { top: 130px; background: var(--paper); }
  .card-back { top: 690px; background: var(--clinic-green); }

  .clinic-mark {
    position: absolute;
    display: flex;
    flex-direction: column;
    align-items: center;
  }
  .clinic-mark .mark-dot {
    border-radius: 50%;
  }
  .clinic-mark .mark-name {
    font-family: "Noto Sans JP", sans-serif;
    font-weight: 500;
    letter-spacing: 1px;
  }
  .card-front .clinic-mark { left: 40px; top: 80px; width: 190px; }
  .card-front .mark-dot { width: 130px; height: 150px; background: var(--clinic-green); margin-bottom: 14px; border-radius: 50%; }
  .card-front .mark-name { font-size: 24px; color: var(--clinic-green); }

  .divider {
    position: absolute;
    left: 232px; top: 62px;
    width: 3px; height: 240px;
    background: var(--clinic-green);
  }
  .staff {
    position: absolute;
    left: 252px; top: 58px;
  }
  .staff-role { font-size: 13px; color: var(--ink); }
  .staff-name {
    font-family: "Noto Serif JP", serif;
    font-size: 30px;
    letter-spacing: 6px;
    line-height: 1.25;
  }
  .staff-romaji { font-family: "Noto Serif JP", serif; font-size: 11px; color: var(--ink-soft); }

  .contacts {
    position: absolute;
    left: 252px; top: 162px;
    list-style: none;
    font-size: 14px;
    color: var(--ink);
  }
  .contacts li { display: flex; align-items: center; height: 27px; }
  .contacts .pair { display: flex; gap: 28px; }
  .contacts .pair span { display: flex; align-items: center; }
  .contacts svg { width: 15px; height: 15px; margin-right: 8px; fill: var(--clinic-green); flex: none; }
  .contacts .address { font-size: 12px; }

  .card-back .clinic-mark { left: 0; width: 600px; top: 98px; }
  .card-back .mark-dot { width: 96px; height: 110px; background: var(--paper); margin-bottom: 16px; border-radius: 50%; }
  .card-back .mark-name { font-size: 24px; color: var(--paper); }
</style>
</head>
<body>
  <div class="side-label" style="top:92px">表</div>
  <section class="card card-front">
    <div class="clinic-mark">
      <div class="mark-dot"></div>
      <div class="mark-name">桜川歯科医院</div>
    </div>
    <div class="divider"></div>
    <div class="staff">
      <div class="staff-role">院長</div>
      <div class="staff-name">山田　一郎</div>
      <div class="staff-romaji">Yamada Ichiro</div>
    </div>
    <ul class="contacts">
      <li class="pair">
        <span><svg viewBox="0 0 16 16"><path d="M3 1h3l1.5 4-2 1.3a9 9 0 0 0 4.2 4.2L11 8.5l4 1.5v3a2 2 0 0 1-2 2A13 13 0 0 1 1 3a2 2 0 0 1 2-2z"/></svg>03-4567-8901</span>
        <span><svg viewBox="0 0 16 16"><path d="M4 1h7v4H4zM1 6h14v7h-3v2H4v-2H1zM5 10v4h6v-4z"/></svg>03-4567-8901</span>
      </li>
      <li><svg viewBox="0 0 16 16"><path d="M1 3h14v10H1zM2 4.5v.6l6 4 6-4v-.6z"/></svg>ichiro@sakuragawa-dc.jp</li>
      <li><svg viewBox="0 0 16 16"><path d="M8 1l7 6.5h-2V15H9.5v-4h-3v4H3V7.5H1z"/></svg>http://www.sakuragawa-dc.jp</li>
      <li class="address"><svg viewBox="0 0 16 16"><path d="M8 1a5 5 0 0 1 5 5c0 4-5 9-5 9S3 10 3 6a5 5 0 0 1 5-5zm0 3a2 2 0 1 0 0 4 2 2 0 0 0 0-4z"/></svg>〒150-0001 東京都渋谷区神宮前1-2-3</li>
    </ul>
  </section>

  <div class="side-label" style="top:652px">裏</div>
  <section class="card card-back">
    <div class="clinic-mark">
      <div class="mark-dot"></div>
      <div class="mark-name">桜川歯科医院</div>
    </div>
  </section>
</body>
</html>
```